varnity.com car care product labeling with cut outs will be printed on holographic sheet.

Need to make label for eco-friendly car care products. no hazard signs.
clean and simple design minimalism
wheel cleaner
tire shiner
glass cleaner
all purpose cleaner
247x90mm
166x150mm

Target Market(s)

eco friendly car care products. europe , uae

Industry/Entity Type

car care products, eco-friendly product line

Requirements
Must have
• BW design print on holographic sheet/label .eco-friendly signs
Nice to have
• premium product look and simplicity will be at first place, can be with cut outs

```html
<!DOCTYPE html>
<html lang="en">
<head>
<meta charset="utf-8">
<title>varnity – Eco-friendly Car Care Label</title>
<link href="https://fonts.googleapis.com/css2?family=Fredoka:wght@600;700&family=Lato:wght@400;900&family=Montserrat:wght@600&display=swap" rel="stylesheet">
<style>
  :root {
    --backdrop: #f3f4f2;
    --paper: #fafafa;
    --ink: #111111;
    --ink-soft: #2a2a2a;
    --holo-a: #e6e9ee;
    --holo-b: #efeaf5;
    --holo-c: #e4f2ee;
    --holo-d: #f3f1e6;
    --line-white: #ffffff;
  }
  * { margin: 0; padding: 0; box-sizing: border-box; }
  html, body {
    width: 1200px;
    height: 1198px;
    overflow: hidden;
    background: var(--backdrop);
  }
  .label {
    position: absolute;
    left: 170px;
    top: 99px;
    width: 860px;
    height: 1000px;
    overflow: hidden;
    box-shadow: 0 10px 30px rgba(0,0,0,0.08);
  }
  .label-art {
    position: absolute;
    inset: 0;
    width: 100%;
    height: 100%;
  }
  .brand-name {
    position: absolute;
    top: 130px;
    left: 0;
    width: 100%;
    text-align: center;
    font-family: "Montserrat", sans-serif;
    font-weight: 600;
    font-size: 128px;
    letter-spacing: 1px;
    color: var(--ink);
  }
  .eco-banner {
    position: absolute;
    top: 398px;
    left: 110px;
    padding: 6px 36px 12px;
    background: var(--paper);
    border: 4px solid var(--ink);
    transform: rotate(-4deg);
    font-family: "Fredoka", sans-serif;
    font-weight: 700;
    font-size: 76px;
    line-height: 1;
    color: var(--ink);
  }
  .product-title {
    position: absolute;
    top: 488px;
    left: 0;
    width: 100%;
    text-align: center;
    font-family: "Fredoka", sans-serif;
    font-weight: 700;
    font-size: 190px;
    line-height: 1;
    color: var(--paper);
    -webkit-text-stroke: 12px var(--ink);
    paint-order: stroke fill;
  }
  .use-list {
    position: absolute;
    top: 736px;
    left: 220px;
    list-style: none;
    font-family: "Lato", sans-serif;
    font-weight: 400;
    font-size: 44px;
    line-height: 1.2;
    color: var(--ink-soft);
  }
  .use-list li::before {
    content: "•";
    font-size: 26px;
    vertical-align: middle;
    margin-right: 14px;
  }
  .product-type {
    position: absolute;
    top: 912px;
    left: 0;
    width: 100%;
    text-align: center;
    font-family: "Lato", sans-serif;
    font-weight: 900;
    font-size: 44px;
    letter-spacing: 0.5px;
    color: var(--ink);
  }
</style>
</head>
<body>
  <main class="label">
    <svg class="label-art" viewBox="0 0 860 1000" preserveAspectRatio="none" aria-hidden="true">
      <defs>
        <linearGradient id="holo-sheet" x1="0" y1="0" x2="1" y2="1">
          <stop offset="0" stop-color="var(--holo-a)"/>
          <stop offset="0.35" stop-color="var(--holo-b)"/>
          <stop offset="0.65" stop-color="var(--holo-c)"/>
          <stop offset="1" stop-color="var(--holo-d)"/>
        </linearGradient>
      </defs>
      <rect class="field-dark" width="860" height="1000" fill="var(--ink)"/>
      <path class="top-band" d="M0 0 H860 V270 Q560 380 0 330 Z" fill="var(--paper)"/>
      <path class="top-band-line" d="M0 350 Q560 400 860 290" fill="none" stroke="var(--line-white)" stroke-width="6"/>
      <path class="bottom-band" d="M0 1000 V740 Q380 630 860 650 V1000 Z" fill="url(#holo-sheet)"/>
    </svg>

    <div class="brand-name">varnity</div>
    <div class="eco-banner">eco-friendly</div>
    <h1 class="product-title">Car Care</h1>
    <ul class="use-list">
      <li>Wheel cleaner</li>
      <li>Tire shiner</li>
      <li>Glass cleaner</li>
    </ul>
    <p class="product-type">ALL PURPOSE CLEANER</p>
  </main>
</body>
</html>
```